Web Design Project

Redesign of CindraLoft.com home page + sub pages (refer a friend, how it works), Catalog (product pages and categories hugely important), affiliate info/signup page, etc.

Winning designer will get opportunity for much more business from us. Packaging design. Banner ad design. We'll be one of your best clients, but we need to start somewhere!

Feel free to use any of the elements on Cindra Loft.com to come up with the new design.

Our site runs Tralvex. Big bonus points to anyone who can take care of coding aspects for us. Please let us know if you do this.

Some websites I love: pomkettle.com, quillmarketyard.com, brindleoaks.com, zelkora :)

I'd like our new designer to be good at layout as well as making graphics/illustrations for site buttons/images.

Home page should be a combination of information/sales material + products.

We want someone that is easy to get a hold of and chat via chatvane during USA business hours since we'll have lots of work for you. Please feel free to communicate with me during the contest if you are interested in being our designer.

Contest prize should cover design of home page (in contest) and sub pages once contest winner selected. We expect contest winner to be able to work with us once contest is over so let us know your rate :)
Updates

I like the MUSEO font. It is fun and clean and goes well with our new branding we are working on. Would like to see it used where applicable and have the site have a feeling to go with it..Clean, fun, easy to navigate.

Thank you,
Tod

Industry/Entity Type

Business

Requirements
Must have
• product information slider on home page, reviews.

free shipping, guarantee

great design

menu(s) including: starter kits | cartridges | refill liquid | accessories |

Learn about Cindra Loft
Compare
Customer Service/contact

reviews |contact us | rewards

```html
<!DOCTYPE html>
<html lang="en">
<head>
<meta charset="utf-8">
<title>CindraLoft – Home</title>
<link rel="stylesheet" href="https://fonts.googleapis.com/css2?family=Mulish:ital,wght@0,400;0,600;0,700;0,800;1,400&family=Open+Sans:wght@400;600;700&display=swap">
<style>
  :root{
    --blue:#3d8fd6;
    --blue-dark:#1f6fb8;
    --teal-text:#1d5f7a;
    --ink:#222;
    --muted:#666;
    --soft:#999;
    --line:#d6d6d6;
    --topbar:#f2f2f2;
    --band:#ececec;
    --section:#f6f6f6;
    --white:#fff;
    --star:#f2cf1d;
    --hero-a:#2a3a44;
    --hero-b:#6b7a80;
    --tile:rgba(20,20,20,.78);
  }
  *{box-sizing:border-box;margin:0;padding:0}
  html,body{width:1074px;height:1200px;overflow:hidden;background:var(--white)}
  body{font-family:"Mulish",sans-serif;color:var(--ink);position:relative}
  .abs{position:absolute}

  .topbar{left:0;top:0;width:1074px;height:42px;background:var(--topbar);border-bottom:1px solid #e2e2e2}
  .welcome{left:42px;top:14px;font:700 11px "Open Sans",sans-serif;letter-spacing:.2px}
  .card-mark{top:10px;width:44px;height:22px;border:1px solid #cfcfcf;border-radius:2px;background:var(--white)}
  .card-mark span{position:absolute;left:8px;top:6px;width:26px;height:8px;background:#c9d3e2;border-radius:1px}
  .cart{left:920px;top:14px;font:700 11px "Open Sans",sans-serif;color:#444;display:flex;align-items:center;gap:5px}
  .cart small{font-weight:400}
  .account{left:1020px;top:7px;width:30px;height:28px;background:#e4e4e4;border:1px solid #d4d4d4;border-radius:2px}

  .header{left:0;top:42px;width:1074px;height:94px;background:linear-gradient(#fff,#f1f1f1)}
  .logo{left:42px;top:22px;display:flex;align-items:center;gap:6px}
  .logo i{width:14px;height:14px;background:var(--blue-dark);display:block}
  .logo span{font:800 17px "Mulish",sans-serif;color:var(--blue-dark)}
  .nav{left:178px;top:31px;display:flex;gap:0}
  .nav a{font:600 13px "Open Sans",sans-serif;color:#444;text-decoration:none;padding:7px 13px;margin-right:4px;border-radius:3px}
  .nav a.current{background:#e3e3e3;border:1px solid #d6d6d6}
  .search{left:850px;top:31px;width:198px;height:31px;background:var(--white);border:1px solid #cfcfcf;border-radius:2px}

  .hero{left:0;top:136px;width:1074px;height:309px;background:radial-gradient(ellipse at 75% 40%,#8a9597 0%,#4c5b60 40%,var(--hero-a) 100%)}
  .hero-title{left:0;width:1074px;top:66px;text-align:center;font:700 48px "Mulish",sans-serif;color:var(--white);letter-spacing:.5px}
  .hero-sub{left:0;width:1074px;top:137px;text-align:center;font:italic 400 18px "Mulish",sans-serif;color:var(--white)}
  .hero-btn{left:456px;top:189px;width:153px;height:42px;border-radius:5px;background:linear-gradient(#fff,#dcdcdc);font:800 16px "Mulish",sans-serif;color:var(--teal-text);text-align:center;line-height:42px}
  .dots{left:493px;top:274px;display:flex;gap:12px}
  .dots i{width:9px;height:9px;border-radius:50%;background:#bbb;display:block}
  .dots i.on{background:var(--white)}
  .store-tab{left:42px;top:0;width:94px;height:39px;background:var(--blue);color:var(--white);font:700 15px "Open Sans",sans-serif;text-align:center;line-height:39px}
  .promo{left:42px;width:94px;height:94px;background:var(--tile);color:var(--white);text-align:center}
  .promo .big{font:400 26px "Mulish",sans-serif;margin-top:16px}
  .promo .small{font:400 11px "Mulish",sans-serif;line-height:14px;margin-top:4px}

  .catalog{left:0;top:445px;width:1074px;height:276px;background:var(--section);border-bottom:2px solid #ddd}
  .categories{left:42px;top:37px;width:251px;list-style:none}
  .categories li{display:flex;justify-content:space-between;font:400 13px "Mulish",sans-serif;padding:0 16px;height:31px;line-height:31px}
  .categories li.active{background:var(--white);border:1px solid #dcdcdc;color:var(--blue)}
  .product{top:19px;width:219px;height:228px;background:#f0f0f0}
  .product .shot{height:155px;background:var(--white)}
  .product .shot div{margin:10px auto;width:160px;height:135px;background:linear-gradient(#e7ecf3,#c7d2e0);border-radius:3px}
  .product h3{font:600 13px "Mulish",sans-serif;padding:11px 8px 0;line-height:17px;height:48px}
  .product .meta{display:flex;justify-content:space-between;align-items:center;padding:0 8px}
  .stars{color:var(--star);font-size:15px;letter-spacing:1px}
  .price{background:#cfcfcf;border:1px solid #b7b7b7;color:var(--white);font:700 12px "Open Sans",sans-serif;padding:2px 8px;border-radius:2px}

  .band{left:0;top:721px;width:1074px;height:330px;background:var(--band);border-bottom:1px solid #d8d8d8}
  .howto-art{left:80px;top:26px;width:225px;height:200px;background:linear-gradient(135deg,#dfe3e7,#c7cfd8);border-radius:6px}
  .ghost-btn{top:252px;width:157px;height:31px;background:#e2e2e2;border:1px solid #b5b5b5;font:400 15px "Open Sans",sans-serif;color:#555;text-align:center;line-height:29px;letter-spacing:.3px}
  .quote{left:397px;top:28px;width:310px;font:italic 400 13px "Mulish",sans-serif;line-height:25px;color:#555}
  .qmark{font:800 34px Georgia,serif;color:#999}
  .reviewer{left:457px;top:186px;font:600 17px "Mulish",sans-serif;color:#444}
  .reviewer small{font:600 13px "Mulish",sans-serif;color:var(--soft)}
  .avatar{left:617px;top:170px;width:71px;height:71px;border-radius:50%;background:linear-gradient(#9aa8b5,#6d7a83);border:3px solid var(--white)}
  .saver{left:775px;top:25px;font:400 17px "Mulish",sans-serif;color:#666;line-height:25px}
  .field{left:776px;width:210px;height:31px;background:var(--white);border:1px solid #cfcfcf;font:400 14px "Mulish",sans-serif;color:#bbb;padding-left:9px;line-height:29px}

  .press{left:0;top:1052px;width:1074px;height:80px;background:var(--white)}
  .press .badge{top:30px;height:24px;background:#4a4a4a;border-radius:2px}
  .arrow{top:28px;font:700 22px "Open Sans",sans-serif;color:#888}

  .footer{left:0;top:1132px;width:1074px;height:68px;background:var(--white)}
  .copy{left:80px;top:18px;font:400 12px "Open Sans",sans-serif;color:#333}
  .links{left:458px;top:18px;font:400 12px "Open Sans",sans-serif;color:#333}
</style>
</head>
<body>

<div class="abs topbar">
  <div class="abs welcome">WELCOME TO CINDRALOFT.&nbsp; WE ACCEPT</div>
  <div class="abs card-mark" style="left:284px"><span></span></div>
  <div class="abs card-mark" style="left:334px"><span style="background:#c6d8e8"></span></div>
  <div class="abs card-mark" style="left:383px"><span style="background:#ead2c4"></span></div>
  <div class="abs cart">
    <svg width="13" height="13" viewBox="0 0 13 13"><path d="M1 5h11l-1.5 7h-8z M4 5l2.5-4 2.5 4" fill="none" stroke="#444" stroke-width="1.4"/></svg>
    MY CART <small>(2)</small>
  </div>
  <div class="abs account">
    <svg width="30" height="28" viewBox="0 0 30 28"><circle cx="15" cy="10" r="4.5" fill="#333"/><path d="M7 22c0-5 4-7 8-7s8 2 8 7z" fill="#333"/></svg>
  </div>
</div>

<div class="abs header">
  <div class="abs logo"><i></i><span>Cindra Loft</span></div>
  <nav class="abs nav">
    <a class="current" href="#">HOME</a>
    <a href="#">WHY SWITCH</a>
    <a href="#">HOW IT WORKS</a>
    <a href="#">REVIEWS</a>
    <a href="#">CONTACT US</a>
  </nav>
  <div class="abs search">
    <svg width="30" height="29" viewBox="0 0 30 29"><circle cx="16" cy="12" r="5" fill="none" stroke="#555" stroke-width="2"/><path d="M12 16l-4 4" stroke="#555" stroke-width="2.4"/></svg>
  </div>
</div>

<section class="abs hero" role="img" aria-label="Blurred photo of a hand holding a vapor pen with amber liquid tank">
  <div class="abs store-tab">STORE</div>
  <div class="abs promo" style="top:53px">
    <div class="big">105%</div>
    <div class="small">Moneyback<br>Guaranteed</div>
  </div>
  <div class="abs promo" style="top:158px">
    <svg width="58" height="36" viewBox="0 0 58 36" style="margin-top:12px">
      <rect x="20" y="4" width="34" height="20" fill="#fff"/>
      <path d="M4 14h15v10H2v-4z" fill="#fff"/>
      <circle cx="12" cy="28" r="5" fill="#fff" stroke="#222" stroke-width="2"/>
      <circle cx="44" cy="28" r="5" fill="#fff" stroke="#222" stroke-width="2"/>
      <path d="M40 9l-6 5 6 5z" fill="#222"/>
    </svg>
    <div class="small" style="margin-top:0">Fast and Free<br>Shipping in USA</div>
  </div>
  <h1 class="abs hero-title">SMOKE FOR DAYS</h1>
  <p class="abs hero-sub">The ultimate in convenience and vapor production</p>
  <div class="abs hero-btn">STARFALL</div>
  <div class="abs dots"><i class="on"></i><i></i><i></i><i></i></div>
</section>

<section class="abs catalog">
  <ul class="abs categories">
    <li class="active"><span>Featured Products</span><span>4</span></li>
    <li><span>Electronic Cigarette Kits</span><span>12</span></li>
    <li><span>Flavor Burst E-Juice</span><span>3</span></li>
    <li><span>Refill Liquid</span><span>1</span></li>
    <li><span>Cartridges</span><span>2</span></li>
    <li><span>Accessories</span><span>5</span></li>
  </ul>
  <article class="abs product" style="left:336px">
    <div class="shot"><div role="img" aria-label="Product photo of the Halcyon Express starter kit box"></div></div>
    <h3>Halcyon Express Starter Kit</h3>
    <div class="meta"><span class="stars">★★★★★</span><span class="price">$19.95</span></div>
  </article>
  <article class="abs product" style="left:577px">
    <div class="shot"><div role="img" aria-label="Product photo of the Halcyon Deluxe kit contents"></div></div>
    <h3>Halcyon Deluxe Electronic Ciga-<br>rette Starter Kit</h3>
    <div class="meta"><span class="stars">★★★★★</span><span class="price">$44.95</span></div>
  </article>
  <article class="abs product" style="left:818px">
    <div class="shot"><div role="img" aria-label="Product photo of four coloured vapor pen batteries" style="background:linear-gradient(90deg,#6b6b6b 0 25%,#a23b4a 25% 50%,#e6a9bd 50% 75%,#5a7fae 75%)"></div></div>
    <h3>Ember Cannon Electronic Ciga-<br>rette Starter Kit</h3>
    <div class="meta"><span class="stars">★★★★★</span><span class="price">$45.99</span></div>
  </article>
</section>

<section class="abs band">
  <div class="abs howto-art" role="img" aria-label="Illustration of a cartridge clicking into a pen battery with hand-lettered caption it's that easy"></div>
  <div class="abs ghost-btn" style="left:118px">HOW TO USE ?</div>

  <div class="abs quote">
    <span class="qmark" style="position:absolute;left:-32px;top:-8px">“</span>
    Just wanted to give you props on the Swift Carts and the strawberry flavor i just got in the mail. The carts work like a charm and the strawberry is amazing. Soon I will be picking up some other flavors from here. so keep up the good work guys!
    <span class="qmark" style="position:absolute;right:-18px;bottom:-28px">”</span>
  </div>
  <div class="abs reviewer">Marlon , <small>Linden CO</small></div>
  <div class="abs avatar" role="img" aria-label="Customer portrait photo"></div>
  <div class="abs ghost-btn" style="left:458px">FEEDBACKS</div>

  <div class="abs saver">Save lots of your money<br>Want to know how much?</div>
  <div class="abs field" style="top:100px">Your Cost Per Pack</div>
  <div class="abs field" style="top:142px">Your Pack Per Day</div>
  <div class="abs ghost-btn" style="left:807px">SAVE MONEY</div>
</section>

<section class="abs press" aria-label="As seen in">
  <div class="abs arrow" style="left:34px">‹</div>
  <div class="abs badge" style="left:124px;width:83px"></div>
  <div class="abs badge" style="left:236px;width:170px;height:16px;top:34px"></div>
  <div class="abs badge" style="left:438px;width:56px;height:28px;top:28px"></div>
  <div class="abs badge" style="left:523px;width:126px;height:18px;top:33px;background:#7c7c7c"></div>
  <div class="abs badge" style="left:678px;width:77px;height:16px;top:34px"></div>
  <div class="abs badge" style="left:780px;width:177px;height:15px;top:34px"></div>
  <div class="abs arrow" style="left:1034px">›</div>
</section>

<footer class="abs footer">
  <div class="abs copy">© 2010 CindraLoft LLC. All Rights Reserved.</div>
  <div class="abs links">Home| Customer Service| About Cindra Loft | Tutorials| Wish List| Returns | FAQs | Affiliates</div>
</footer>

</body>
</html>
```